Homepage für Unternehmensberatung
Zielgruppe
Wir sind eine Unternehmensberatung mit einem klaren Branchenfokus auf Banken / Finanzdienstleister.
Unsere Dienstleistungsprodukte lassen sich grob in folgende Themencluster unterteilen:
1)Strategieentwicklung
o IT-Strategie, IT-Architektur, IT-Bebauungsplan
2) Projektmanagement
o Projektportfoliomgmt., Programmmgmt., Projektmanagement, Projektcontrolling
3) Fachberatung
o Bankfachliche IT- Beratung mit Schwerpunkten Kredit, Wertpapiergeschäft,
Bankenaufsichtsrecht, Liquiditätsmanagement
o Anforderungsmanagement inkl. Aufbau von Bewertungs- und Priorisierungsmethoden
4) Prozessberatung/-optimierung
o Prozessanalyse, Prozessdesign, Prozessdokumentation
o Prozessoptimierung auf Basis etablierter Messmethoden
Unser Firmenname Lindenhofer hat für uns eine Doppelbedeutung:
1. Im Außenverhältnis: Wir verstehen uns als Lindenhofer unserer Kunden
2. Im Innenverhältnis: Wir pflegen einen partnerschaftlichen Umgang mit unseren
Mitarbeitern (Teamarbeit)
Aktuell sind wir ein kleines aber feines Team von erfahrenen und hochmotivierten Kollegen. Unsere Mitarbeiter sind ehemalige Führungskräfte sowie erfahrenen Unternehmensberater.
Aufgabenstellung
Entwurf / Design von 2 Seiten:
1. Seite / Startseite:
Simple und elegante Darstellung der oben genannten 4 Themencluster (z.B. Bild/Piktogramm, Textkasten) sowie einer Navigationsmöglichkeit zu folgenden Detailsichten:
• Unternehmen
• Beratungsangebot (siehe Themencluster)
• Partnerunternehmen
• Kontakt
2. Seite / 2. Ebene:
Entwurf einer Möglichkeit zur Erläuterung/Darstellung von Inhalten der Startseite.
Die Themencluster sollten auf jeder Ebene immer „anklickbar“/ zu sehen sein.
Logo
Das angehängte Logo ist in die Website einzubinden. Stil und Farben sollen übernommen werden bzw. sind Basis für das Design.
Lizenzen
Lizenz für eingesetzte Fotos und Illustrationen soll enthalten / Open-Source sein. Wenn nicht dann bitte zusätzliche Kosten angeben.

```html
<!DOCTYPE html>
<html lang="de">
<head>
<meta charset="utf-8">
<title>Lindenhofer – Startseite</title>
<link href="https://fonts.googleapis.com/css2?family=Roboto:wght@300;400;500;700&display=swap" rel="stylesheet">
<style>
  :root {
    --brand-blue: #1a7fc1;
    --brand-blue-dark: #156aa3;
    --text-grey: #6b6f73;
    --text-dark: #3a3d40;
    --line: #e6e8ea;
    --page-bg: #ececec;
    --white: #ffffff;
    --hero-dark: #2c2f33;
    --hero-mid: #6d7278;
    --hero-light: #a9adb1;
  }
  * { box-sizing: border-box; margin: 0; padding: 0; }
  html, body { width: 1200px; height: 933px; overflow: hidden; }
  body {
    background: var(--page-bg);
    font-family: "Roboto", Arial, sans-serif;
    color: var(--text-dark);
  }
  .site {
    position: absolute;
    left: 80px; top: 0;
    width: 1040px; height: 933px;
    background: var(--white);
    box-shadow: 0 0 24px rgba(0,0,0,0.08);
  }
  .site-header {
    height: 108px;
    display: flex; align-items: center; justify-content: space-between;
    padding: 0 54px;
  }
  .brand { display: flex; align-items: center; gap: 14px; }
  .brand-dot {
    width: 48px; height: 48px; border-radius: 50%;
    background: var(--brand-blue);
  }
  .brand-name {
    font-size: 27px; font-weight: 400; letter-spacing: 0.5px;
    color: var(--brand-blue); line-height: 1;
  }
  .brand-tagline {
    margin-top: 5px;
    font-size: 8px; letter-spacing: 3px; text-transform: uppercase;
    color: var(--text-grey); font-weight: 300;
  }
  .meta-nav { display: flex; gap: 0; list-style: none; }
  .meta-nav li {
    font-size: 12px; color: var(--text-grey);
    padding: 0 11px; border-left: 1px solid var(--line);
  }
  .meta-nav li:first-child { border-left: none; }
  .main-nav {
    height: 66px;
    border-top: 1px solid var(--line);
    display: flex; align-items: center; gap: 46px;
    padding: 0 42px; list-style: none;
  }
  .main-nav li { font-size: 13px; color: var(--text-grey); }
  .hero {
    position: relative;
    height: 512px;
    background: radial-gradient(ellipse at 55% 30%, var(--hero-light) 0%, var(--hero-mid) 45%, var(--hero-dark) 100%);
    overflow: hidden;
  }
  .hero-caption {
    position: absolute; left: 82px; bottom: 84px;
    color: var(--white);
  }
  .hero-title {
    font-size: 34px; font-weight: 700;
    text-shadow: 0 1px 3px rgba(0,0,0,0.5);
  }
  .hero-text {
    margin-top: 8px; max-width: 540px;
    font-size: 15px; font-weight: 500; line-height: 1.45;
    text-shadow: 0 1px 2px rgba(0,0,0,0.6);
  }
  .hero-button {
    display: inline-block; margin-top: 22px;
    padding: 11px 18px;
    background: rgba(40,44,48,0.85);
    color: var(--white); font-size: 12px; font-weight: 500;
  }
  .services {
    display: flex; height: 247px;
    padding-top: 30px;
  }
  .service {
    flex: 1; display: flex; flex-direction: column; align-items: center;
    border-left: 1px solid var(--line);
    height: 150px;
  }
  .service:first-child { border-left: none; }
  .service-icon {
    width: 108px; height: 108px; border-radius: 50%;
    background: var(--white);
    box-shadow: 0 2px 10px rgba(0,0,0,0.12);
    display: flex; align-items: center; justify-content: center;
  }
  .service-icon svg { width: 50px; height: 50px; }
  .service-label {
    margin-top: 22px;
    font-size: 16px; font-weight: 700; color: var(--brand-blue);
  }
</style>
</head>
<body>
  <div class="site">
    <header class="site-header">
      <div class="brand">
        <span class="brand-dot"></span>
        <div>
          <div class="brand-name">Lindenhofer</div>
          <div class="brand-tagline">Management und Prozessberatung</div>
        </div>
      </div>
      <ul class="meta-nav">
        <li>Home</li><li>Karriere</li><li>Aktuelles</li><li>Kontakt</li>
      </ul>
    </header>

    <ul class="main-nav">
      <li>Unternehmen</li><li>Beratungsangebot</li><li>Partnerunternehmen</li>
    </ul>

    <section class="hero" role="img" aria-label="Foto: Team von Beratern in Anzügen vor einer grauen Weltkarte">
      <div class="hero-caption">
        <h1 class="hero-title">Projektmanagement</h1>
        <p class="hero-text">Der Aufbau einer neuen IT-Organisation in einer Tochtergesellschaft, die Restrukturierung eines IT-Bereiches.</p>
        <span class="hero-button">Mehr erfahren →</span>
      </div>
    </section>

    <section class="services">
      <div class="service">
        <div class="service-icon">
          <svg viewBox="0 0 50 50" fill="none" stroke="var(--brand-blue)" stroke-width="4" stroke-linecap="round">
            <line x1="12" y1="40" x2="36" y2="16"/>
            <line x1="38" y1="40" x2="16" y2="18"/>
            <path d="M10 12 l8 -4 l6 6 l-4 8 z" fill="var(--brand-blue)"/>
            <circle cx="38" cy="12" r="5"/>
          </svg>
        </div>
        <div class="service-label">Strategieentwicklung</div>
      </div>
      <div class="service">
        <div class="service-icon">
          <svg viewBox="0 0 50 50" fill="none" stroke="var(--brand-blue)" stroke-width="3" stroke-linejoin="round">
            <path d="M6 12 L25 16 L44 12 L44 40 L25 44 L6 40 Z"/>
            <line x1="25" y1="16" x2="25" y2="44"/>
            <line x1="11" y1="22" x2="20" y2="24"/><line x1="11" y1="29" x2="20" y2="31"/>
            <line x1="30" y1="24" x2="39" y2="22"/><line x1="30" y1="31" x2="39" y2="29"/>
          </svg>
        </div>
        <div class="service-label">Projektmanagement</div>
      </div>
      <div class="service">
        <div class="service-icon">
          <svg viewBox="0 0 50 50" fill="var(--brand-blue)">
            <circle cx="19" cy="17" r="8"/>
            <path d="M4 42 Q4 27 19 27 Q34 27 34 42 Z"/>
            <circle cx="34" cy="15" r="6"/>
            <path d="M30 24 Q46 22 46 38 L37 38 Q37 29 30 24 Z"/>
          </svg>
        </div>
        <div class="service-label">Fachberatung</div>
      </div>
      <div class="service">
        <div class="service-icon">
          <svg viewBox="0 0 50 50" fill="none" stroke="var(--brand-blue)" stroke-width="3.5" stroke-linecap="round">
            <path d="M19 33 Q19 28 15 23 A11 11 0 1 1 35 23 Q31 28 31 33 Z"/>
            <line x1="20" y1="39" x2="30" y2="39"/>
            <line x1="22" y1="44" x2="28" y2="44"/>
          </svg>
        </div>
        <div class="service-label">Prozessberatung</div>
      </div>
    </section>
  </div>
</body>
</html>
```